New Business Card Design Project

We require a business card design for Pharvelix, a newly established Indian company.
Our focus is on the development, manufacturing, and export of a diverse array of pharmaceutical products on a global scale. The card should convey a professional appearance, as our primary markets are in Africa, China, and Southeast Asian nations.
We envision a two-sided business card, with the reverse side dedicated to a logo set against a solid color or an elegantly designed pattern. The corners should be rounded. We would appreciate seeing both horizontal and vertical design options. We trust the designer to utilize their expertise in creating this design.

The content for the business card is included in the attached Word file.

Target Market(s)

Our primary markets are in Africa, China, and Southeast Asian, Latin America, Maldives, Sri Lanka

Industry/Entity Type

Pharmaceutical Manufacturing and Export

Contact Information for Business Card

Colors

Designer to choose colors to be used in the design.

Requirements
Must have
• The reverse side of the business card features solely the logo along with the tagline, "Wellness for All."
Should not have
• The logo should not exceed two instances, encompassing both the front and back sides of the card.

```html
<!DOCTYPE html>
<html lang="en">
<head>
<meta charset="utf-8">
<title>Pharvelix Business Card</title>
<link rel="stylesheet" href="https://fonts.googleapis.com/css2?family=Open+Sans:wght@400;700&family=Poppins:wght@400;600&display=swap">
<style>
  :root {
    --stage: #222222;
    --card: #ffffff;
    --brand-blue: #2ea8df;
    --brand-coral: #f06650;
    --ink: #1d1d1d;
  }
  * { margin: 0; padding: 0; box-sizing: border-box; }
  html, body {
    width: 1200px; height: 711px; overflow: hidden;
    background: var(--stage);
  }
  .stage { position: relative; width: 1200px; height: 711px; }
  .card {
    position: absolute; left: 341px; width: 518px; height: 296px;
    background: var(--card); border-radius: 24px;
    box-shadow: 0 8px 22px rgba(0,0,0,0.6);
    overflow: hidden;
  }
  .card--front { top: 36px; }
  .card--back { top: 362px; }

  .brand-dot {
    position: absolute; left: 50%; top: 72px; width: 70px; height: 70px;
    margin-left: -35px; border-radius: 50%; background: var(--brand-coral);
  }
  .brand-name {
    position: absolute; left: 0; right: 0; top: 172px; text-align: center;
    font-family: "Poppins", sans-serif; font-weight: 600; font-size: 52px;
    line-height: 1; color: var(--brand-blue); letter-spacing: -0.5px;
  }
  .tagline {
    position: absolute; left: 0; right: 0; top: 263px; text-align: center;
    font-family: "Poppins", sans-serif; font-size: 13px; color: var(--ink);
  }

  .holder {
    position: absolute; left: 30px; width: 197px; top: 126px; text-align: right;
    font-family: "Open Sans", sans-serif;
  }
  .holder-name {
    font-size: 22px; line-height: 1.1; color: var(--brand-blue); white-space: nowrap;
  }
  .holder-name strong { font-weight: 700; }
  .holder-role { font-size: 15px; color: var(--ink); margin-top: 2px; }

  .divider {
    position: absolute; left: 259px; top: 104px; width: 1px; height: 90px;
    background: var(--brand-coral);
  }
  .contacts {
    position: absolute; left: 297px; top: 118px; list-style: none;
    font-family: "Open Sans", sans-serif; font-size: 14px; color: var(--ink);
  }
  .contacts li { display: flex; align-items: center; height: 17.5px; white-space: nowrap; }
  .contacts svg { width: 13px; height: 13px; margin-right: 7px; flex: none; }
  .address {
    position: absolute; left: 0; right: 0; top: 255px; text-align: center;
    font-family: "Open Sans", sans-serif; font-size: 13.5px; color: var(--ink);
  }
</style>
</head>
<body>
<main class="stage">
  <section class="card card--front">
    <span class="brand-dot"></span>
    <h1 class="brand-name">Pharvelix</h1>
    <p class="tagline">Wellness for All.</p>
  </section>

  <section class="card card--back">
    <div class="holder">
      <p class="holder-name"><strong>Arjun</strong> K. Mehta</p>
      <p class="holder-role">CEO</p>
    </div>
    <span class="divider"></span>
    <ul class="contacts">
      <li>
        <svg viewBox="0 0 13 13" aria-hidden="true"><rect x="3" y="0.8" width="7" height="11.4" rx="1" fill="none" stroke="var(--brand-coral)" stroke-width="1.4"/></svg>
        +91 98765 43210
      </li>
      <li>
        <svg viewBox="0 0 13 13" aria-hidden="true"><circle cx="6.5" cy="6.5" r="6" fill="var(--brand-blue)"/><path d="M3 4.5 Q5 3 6 5 T9 8 M7 10 Q8 9 10 10" fill="none" stroke="#fff" stroke-width="1.2"/></svg>
        www.pharvelix.com
      </li>
      <li>
        <svg viewBox="0 0 13 13" aria-hidden="true"><rect x="0.5" y="4" width="12" height="8.5" fill="var(--brand-coral)"/><path d="M0.5 4 L6.5 8.5 L12.5 4" fill="none" stroke="#fff" stroke-width="1"/><circle cx="6.5" cy="3.5" r="2.5" fill="#fff" stroke="var(--brand-coral)" stroke-width="1"/></svg>
        amehta@pharvelix.com
      </li>
    </ul>
    <p class="address">12, Lotus Park Road, Nashik, 422005, India</p>
  </section>
</main>
</body>
</html>
```